Popup Banners - BrightCounsel - Legal Technology

- We need two banners (same style) designed with two different images and different text.

- The details of the printing requirements are attached, along with suggested images.

- The banners should share the same theme as our website www.brightcounsel.com.au

- The first banner would include our logo (attached), use the 'roads join' image (attached) in some way and text: New Opportunities - Where legal services and technology meet.

- The second banner would include our logo (attached), use the 'jigsaw' image (attached) in some way and use text: Legal Technology Strategy, Advice and Capability.

- Details on what are required from the Printer is attached also.

Target Market(s)

Legal Professionals

Industry/Entity Type

Information Technology

Font styles to use
Sans Serif

Requirements
Must have
• Our logo (attached), suggested text and the image mentioned for each.
Nice to have
• Professional and modern look
Should not have
• Cheap looking

```html
<!DOCTYPE html>
<html lang="en">
<head>
<meta charset="utf-8">
<title>BrightCounsel – Legal Technology Banner</title>
<link rel="stylesheet" href="https://fonts.googleapis.com/css2?family=Open+Sans:wght@400;700;800&display=swap">
<style>
  :root {
    --stage: #121212;
    --paper: #ffffff;
    --navy: #0c2240;
    --ink: #4a4544;
    --taupe: #6e6662;
    --accent: #4a9fd8;
    --photo-light: #dbe9f3;
    --photo-mid: #6a93b3;
    --photo-dark: #1f4566;
  }
  * { margin: 0; padding: 0; box-sizing: border-box; }
  html, body { width: 1200px; height: 1200px; overflow: hidden; background: var(--stage); }
  .canvas { position: relative; width: 1200px; height: 1200px; background: var(--stage); }
  .banner {
    position: absolute; left: 373px; top: 40px; width: 454px; height: 1120px;
    background: var(--navy); font-family: "Open Sans", sans-serif; overflow: hidden;
  }
  .brand-bar {
    height: 134px; background: var(--paper);
    display: flex; align-items: center; justify-content: center; gap: 18px;
  }
  .brand-mark { width: 22px; height: 22px; background: var(--accent); }
  .brand-name {
    font-size: 38px; font-weight: 400; color: var(--ink); letter-spacing: 0.22em;
  }
  .hero-photo {
    height: 626px;
    background: radial-gradient(ellipse at 62% 60%, var(--photo-light) 0%, var(--photo-mid) 40%, var(--photo-dark) 80%);
  }
  .message-band {
    height: 202px; position: relative; background: var(--navy);
    display: flex; flex-direction: column; align-items: center; padding-top: 24px;
  }
  .headline {
    color: var(--paper); font-weight: 800; font-size: 28px; line-height: 37px;
    letter-spacing: 0.12em; text-align: center; text-transform: uppercase;
  }
  .web-tab {
    position: absolute; bottom: 0; left: 50%; transform: translateX(-50%);
    width: 301px; height: 47px; border-radius: 12px 12px 0 0;
    background: linear-gradient(#8a8280, var(--taupe));
    color: var(--paper); font-size: 27px; line-height: 47px; text-align: center;
  }
  .phone-band {
    height: 95px; background: var(--paper);
    display: flex; align-items: center; justify-content: center; gap: 12px;
  }
  .phone-icon { width: 22px; height: 30px; }
  .phone-number {
    color: var(--ink); font-weight: 700; font-size: 38px; letter-spacing: 0.09em;
  }
  .base-band { height: 63px; background: var(--navy); position: relative; }
  .base-rule {
    position: absolute; top: 0; left: 67px; width: 321px; height: 13px; background: var(--taupe);
  }
</style>
</head>
<body>
<div class="canvas">
  <div class="banner">
    <header class="brand-bar">
      <span class="brand-mark"></span>
      <span class="brand-name">BrightCounsel</span>
    </header>
    <div class="hero-photo" role="img" aria-label="Backlit photograph of fingers placing a jigsaw puzzle piece, in cool blue tones"></div>
    <section class="message-band">
      <h1 class="headline">Legal Technology<br>Strategy, Advice<br>and Capability</h1>
      <div class="web-tab">brightcounsel.com.au</div>
    </section>
    <div class="phone-band">
      <svg class="phone-icon" viewBox="0 0 22 30" aria-hidden="true">
        <path d="M7 2 L10 8 L7 11 Q8 17 12 21 L15 18 L20 22 L17 27 Q4 25 2 8 Z" fill="none" stroke="#4a4544" stroke-width="2.4" stroke-linejoin="round"/>
      </svg>
      <span class="phone-number">07 3555 0199</span>
    </div>
    <div class="base-band"><span class="base-rule"></span></div>
  </div>
</div>
</body>
</html>
```